Infographic & Data Visualisation Design for – Australia’s Yearly Harmwatch Review 2026

About Carrowby Institute: Carrowby Institute is an independent non-profit public health organization. We produce Australia’s Yearly Harmwatch Review, which translates verified national mortality data into actionable insights for policymakers, journalists, healthcare workers, and the general public.

Project Goal: We need a suite of high-impact, clean, and authoritative infographics and data visualisations created for Australia’s Yearly Harmwatch Review 2026.

What We Are Providing:

Full Dataset (.xlsx): Complete Excel file containing all 2026 report data.

Data & Chart Guidance Doc (.docx): A summary document detailing each dataset, the core takeaway, and our initial recommendations for chart types (e.g., line graphs, horizontal bar charts, donut charts, metric tiles).

Carrowby Institute Brand Book (.pdf): Complete brand guidelines covering fonts, colors, line weights, and imagery. These guidelines and in particular colours should be used across the infographics.

Previous Year Reference: You can view how last year’s report and graphics here: https://www.carrowby-example.org.au/australias-yearly-harmwatch-review-2025/

Designer Input & Creative Freedom: While we have provided a guide suggesting specific chart types for each dataset, we are not data visualisation experts - you are! We are very open to your creative ideas, structural suggestions, and design expertise. If you identify a clearer, more engaging, or visually compelling way to illustrate a specific dataset, we welcome your input.

Required Deliverables:

Master Report Infographics: High-resolution, print/PDF-ready A4 vector graphics for the formal report publication (Delivered as vector AI/EPS and high-res PDF/PNG).

Web Assets: Web-optimized PNG/SVG files with transparent or brand backgrounds.

Social Media Adaptations: 1:1 (Square) and 4:5 / 9:16 (Vertical) graphic cards for Pictoral, WorkMesh, Chatterly, and X.
Updates

Deadline was too tight - have extended it to ensure the designers have enough time to do the job.

Target Market(s)

Policy makers, journalists, health sector professionals, frontline workers, and the general public.

Industry/Entity Type

Drug/Government/Not for Profit

Font styles to use
Sans Serif
Other font styles liked:
• Brand Fonts: Use any or a combination of: Host Grotesk or Libre Baskerville or Poppins or Calibri Light

Colors

Designer to choose colors to be used in the design.

Requirements
Must have
• The ability to create Infographics, graphs of all kinds from data that we have given.
Nice to have
• Help with choosing what infographics/graphs/donuts graphs etc will be best to visualise the data.
Should not have
• A designer who has not made graphs or infographics from Data.

```html
<!DOCTYPE html>
<html lang="en">
<head>
<meta charset="utf-8">
<title>Historic Highs – Australia’s Yearly Harmwatch Review 2026</title>
<link href="https://fonts.googleapis.com/css2?family=Arimo:wght@400;500;600;700&display=swap" rel="stylesheet">
<style>
  :root{
    --navy:#0b2549;
    --navy-track:#2a4a72;
    --orange:#ff773b;
    --periwinkle:#5b74fb;
    --sky:#1a95f2;
    --purple:#6e22b0;
    --plum:#5e1440;
    --ink:#0b2549;
    --grey:#555b66;
    --rule:#d8d8d8;
    --pale:#e3ecfb;
    --white:#ffffff;
  }
  *{margin:0;padding:0;box-sizing:border-box;}
  html,body{width:849px;height:1200px;overflow:hidden;background:var(--white);}
  body{font-family:"Arimo",Arial,sans-serif;color:var(--ink);}
  .canvas{position:relative;width:849px;height:1200px;overflow:hidden;}
  .abs{position:absolute;}
  .backdrop{position:absolute;left:0;top:0;}

  /* left panel */
  .report-title{left:43px;top:36px;color:var(--white);font-size:13px;letter-spacing:1.6px;line-height:17px;text-transform:uppercase;}
  .title-rule{left:43px;top:80px;width:185px;height:3px;background:var(--sky);}
  .year{left:38px;top:100px;font-size:106px;font-weight:400;line-height:110px;color:transparent;-webkit-text-stroke:1.6px var(--orange);letter-spacing:-1px;}
  .kicker{left:43px;top:216px;color:var(--white);font-size:24px;letter-spacing:.5px;}
  .headline-left{left:42px;top:246px;font-size:38px;font-weight:700;line-height:40px;color:var(--white);}
  .headline-left .accent{color:var(--orange);}
  .lede{left:43px;top:333px;color:var(--white);font-size:13px;line-height:17px;}
  .big-count{left:42px;top:372px;color:var(--white);font-size:74px;font-weight:700;line-height:76px;letter-spacing:-1px;}
  .big-count-label{left:45px;top:447px;color:var(--white);font-size:17px;}
  .pill{height:25px;border-radius:13px;font-size:8.5px;letter-spacing:1.6px;line-height:25px;text-align:center;text-transform:uppercase;}
  .pill-orange{left:43px;top:479px;width:183px;background:var(--orange);color:var(--navy);}
  .pill-pale{left:43px;top:651px;width:167px;height:24px;line-height:24px;background:var(--pale);color:var(--navy);}
  .left-divider{left:43px;top:545px;width:196px;height:1px;background:#3e5a82;}
  .rate{left:42px;top:556px;color:var(--sky);font-size:64px;font-weight:700;line-height:66px;}
  .rate-label{left:43px;top:619px;color:var(--white);font-size:15px;}
  .states-title{left:43px;top:753px;color:var(--orange);font-size:11.5px;letter-spacing:1.8px;}
  .states-sub{left:43px;top:773px;color:var(--white);font-size:11px;}
  .state-row{left:43px;width:220px;height:14px;}
  .state-name{position:absolute;left:0;top:0;color:var(--white);font-size:11px;font-weight:700;letter-spacing:1.3px;line-height:14px;}
  .state-track{position:absolute;left:36px;top:1px;width:147px;height:13px;border-radius:7px;background:var(--navy-track);}
  .state-fill{position:absolute;left:0;top:0;height:13px;border-radius:7px;}
  .state-value{position:absolute;left:195px;top:-2px;color:var(--white);font-size:14px;font-weight:700;}
  .note{left:66px;top:1023px;color:var(--white);font-size:10px;line-height:14px;}
  .note-icon{left:44px;top:1026px;width:15px;height:15px;border-radius:50%;background:var(--orange);color:var(--white);font-size:11px;font-weight:700;text-align:center;line-height:15px;}

  /* right panel */
  .org{left:709px;top:29px;font-size:10px;font-weight:700;letter-spacing:2px;line-height:13px;color:var(--navy);}
  .story-tag{left:374px;top:59px;color:var(--periwinkle);font-size:11px;letter-spacing:1.6px;}
  .headline{left:373px;top:94px;font-weight:700;line-height:37px;}
  .headline .line-1{display:block;font-size:31px;color:var(--navy);letter-spacing:.3px;}
  .headline .line-2{display:block;font-size:37px;color:var(--purple);}
  .dek{left:374px;top:182px;color:var(--grey);font-size:12.5px;line-height:18px;}
  .rule{height:1px;background:var(--rule);}
  .rule-top{left:371px;top:227px;width:454px;}
  .axis-title{left:373px;top:286px;font-size:9.5px;letter-spacing:1.8px;color:var(--navy);}
  .chart{left:360px;top:360px;}
  .chart text{font-family:"Arimo",Arial,sans-serif;}
  .rule-bottom{left:370px;top:991px;width:454px;}

  .callout{left:372px;top:1018px;width:437px;height:110px;border-radius:14px;background:var(--navy);overflow:hidden;}
  .callout-bar{position:absolute;left:0;top:0;width:16px;height:100%;background:var(--orange);}
  .callout-kicker{position:absolute;left:26px;top:23px;color:#9fc3f5;font-size:10px;letter-spacing:1.8px;}
  .callout-text{position:absolute;left:26px;top:41px;color:var(--white);font-size:18px;line-height:21px;}
  .callout-note{position:absolute;left:26px;top:87px;color:#d5def0;font-size:10px;}

  .source-rule{left:372px;top:1154px;width:437px;height:1.5px;background:var(--navy);}
  .source{left:373px;top:1165px;font-size:8.5px;font-weight:700;color:var(--navy);}
  .method{left:373px;top:1180px;font-size:8px;color:var(--grey);}
  .footer-tag{left:373px;top:1192px;font-size:8px;letter-spacing:1.5px;color:var(--periwinkle);}
</style>
</head>
<body>
<div class="canvas">

  <svg class="backdrop" width="849" height="1200" viewBox="0 0 849 1200" aria-hidden="true">
    <polygon points="0,0 336,0 275,1200 0,1200" fill="var(--navy)"/>
    <polygon points="336,0 347,0 288,1200 275,1200" fill="var(--orange)"/>
    <polygon points="347,0 353,0 293,1200 288,1200" fill="var(--periwinkle)"/>
    <circle cx="36" cy="968" r="135" fill="none" stroke="#163a6a" stroke-width="1.5"/>
  </svg>

  <!-- left panel -->
  <div class="abs report-title">Australia’s Yearly Harmwatch<br>Review 2026</div>
  <div class="abs title-rule"></div>
  <div class="abs year">2024</div>
  <div class="abs kicker">A YEAR OF</div>
  <h1 class="abs headline-left">HISTORIC<br><span class="accent">HIGHS.</span></h1>
  <p class="abs lede">Unintentional drug-induced deaths<br>reached record levels in Australia.</p>
  <div class="abs big-count">2,091</div>
  <div class="abs big-count-label">unintentional deaths</div>
  <div class="abs pill pill-orange">Highest number since 2001</div>
  <div class="abs left-divider"></div>
  <div class="abs rate">7.6</div>
  <div class="abs rate-label">deaths per 100,000 people</div>
  <div class="abs pill pill-pale">Highest rate since 2001</div>

  <div class="abs states-title">STATE RECORD COUNTS</div>
  <div class="abs states-sub">Highest annual totals since 2001</div>

  <div class="abs state-row" style="top:805px">
    <span class="state-name">VIC</span>
    <span class="state-track"><span class="state-fill" style="width:147px;background:var(--orange)"></span></span>
    <span class="state-value">572</span>
  </div>
  <div class="abs state-row" style="top:835px">
    <span class="state-name">QLD</span>
    <span class="state-track"><span class="state-fill" style="width:107px;background:var(--periwinkle)"></span></span>
    <span class="state-value">417</span>
  </div>
  <div class="abs state-row" style="top:866px">
    <span class="state-name">WA</span>
    <span class="state-track"><span class="state-fill" style="width:71px;background:var(--sky)"></span></span>
    <span class="state-value">278</span>
  </div>
  <div class="abs state-row" style="top:896px">
    <span class="state-name">SA</span>
    <span class="state-track"><span class="state-fill" style="width:41px;background:var(--purple)"></span></span>
    <span class="state-value">157</span>
  </div>

  <div class="abs note-icon">!</div>
  <p class="abs note">All figures on this page refer to<br>unintentional drug-induced deaths.</p>

  <!-- right panel -->
  <div class="abs org">CARROWBY<br>INSTITUTE</div>
  <div class="abs story-tag">DATA STORY 03 / HISTORIC HIGHS</div>
  <h2 class="abs headline"><span class="line-1">THREE DRUG CATEGORIES</span><span class="line-2">HIT NEW HIGHS.</span></h2>
  <p class="abs dek">Annual unintentional deaths involving each drug type,<br>comparing 2001 with the record level reached in 2024.</p>
  <div class="abs rule rule-top"></div>
  <div class="abs axis-title">NUMBER OF DEATHS</div>

  <svg class="abs chart" width="489" height="630" viewBox="360 360 489 630" role="img" aria-label="Stacked bar chart of deaths in 2001 and 2024 by drug type">
    <g stroke="#d9d9d9" stroke-width="1">
      <line x1="399" y1="446" x2="819" y2="446"/>
      <line x1="399" y1="553" x2="560" y2="553"/>
      <line x1="668" y1="553" x2="819" y2="553"/>
      <line x1="399" y1="660" x2="819" y2="660"/>
      <line x1="399" y1="767" x2="819" y2="767"/>
    </g>
    <g font-size="10" fill="#666" text-anchor="end">
      <text x="387" y="450">800</text>
      <text x="387" y="557">600</text>
      <text x="387" y="664">400</text>
      <text x="387" y="771">200</text>
      <text x="387" y="878">0</text>
    </g>
    <!-- cocaine -->
    <rect x="428" y="799" width="93" height="59" fill="var(--plum)"/>
    <rect x="428" y="860" width="93" height="14" fill="var(--navy)"/>
    <!-- heroin -->
    <rect x="567" y="606" width="93" height="207" fill="var(--orange)"/>
    <rect x="567" y="815" width="93" height="59" fill="var(--navy)"/>
    <!-- amphetamine-type stimulants -->
    <rect x="712" y="462" width="95" height="384" fill="var(--sky)"/>
    <rect x="712" y="848" width="95" height="26" fill="var(--navy)"/>
    <line x1="399" y1="874" x2="819" y2="874" stroke="var(--navy)" stroke-width="1.8"/>

    <g text-anchor="middle">
      <text x="474" y="745" font-size="21" font-weight="700" fill="var(--plum)">141</text>
      <text x="474" y="765" font-size="11" fill="var(--navy)">5.0× SINCE 2001</text>
      <text x="617" y="560" font-size="21" font-weight="700" fill="var(--orange)">488</text>
      <text x="617" y="580" font-size="11" fill="var(--navy)">4.8× SINCE 2001</text>
      <text x="760" y="395" font-size="23" font-weight="700" fill="var(--sky)">772</text>
      <text x="760" y="416" font-size="12" font-weight="700" fill="var(--navy)">14.6×</text>
      <text x="760" y="430" font-size="8.5" font-weight="700" letter-spacing="1.6" fill="var(--navy)">SINCE 2001</text>

      <g font-size="11.5" font-weight="700" letter-spacing="1.8" fill="var(--navy)">
        <text x="474" y="913">COCAINE</text>
        <text x="617" y="913">HEROIN</text>
        <text x="760" y="913">AMPHETAMINE-TYPE</text>
        <text x="760" y="929">STIMULANTS</text>
      </g>
      <text x="474" y="934" font-size="9.5" fill="var(--plum)">2001: 28 2024: 141</text>
      <text x="617" y="934" font-size="9.5" fill="var(--orange)">2001: 101 2024: 488</text>
      <text x="749" y="950" font-size="9.5" fill="var(--sky)">2001: 53 2024: 772</text>
    </g>

    <rect x="407" y="967" width="13" height="10" fill="var(--navy)"/>
    <text x="425" y="977" font-size="10" fill="#444">2001 level</text>
    <rect x="496" y="967" width="5" height="10" fill="var(--plum)"/>
    <rect x="501" y="967" width="4" height="10" fill="var(--orange)"/>
    <rect x="505" y="967" width="5" height="10" fill="var(--sky)"/>
    <text x="517" y="977" font-size="10" fill="#444">Growth to 2024 record</text>
  </svg>

  <div class="abs rule rule-bottom"></div>

  <div class="abs callout">
    <div class="callout-bar"></div>
    <div class="callout-kicker">THE LONG VIEW</div>
    <p class="callout-text">The overall toll more than doubled<br>from 981 deaths in 2001 to 2,091 in 2024.</p>
    <p class="callout-note">Drug-type categories can overlap and should not be summed.</p>
  </div>

  <div class="abs source-rule"></div>
  <p class="abs source">Source: Carrowby Institute, Australia’s Yearly Harmwatch Review 2026 dataset.</p>
  <p class="abs method">Historic highs are measured against annual data from 2001. Rate is per 100,000 people.</p>
  <p class="abs footer-tag">HISTORIC HIGHS / 2024 NATIONAL SNAPSHOT</p>

</div>
</body>
</html>
```